Redesign of existing Web Design Project

I wish to redsesign the web pages on www.bqrl.com.au

Background of Halvern Oakridge

Halvern Oakridge Construction Services was established in 2004 as a boutique construction company offering construction advice and management services. We assist people in the construction minefield – step by step.

We offer services in: -

• Construction Management
• Project Management
• Building

The essence of our business is ensuring every project we undertake achieves the client’s objectives. Our experience has shown the secrets to a profitable project are -

• Planning
• Attention to detail
• Value add

We take the trouble to understand the client’s needs in person. Our hands-on approach ensures those involved deliver to the required quality standards at the scheduled times.

Our area of works include: -

• Residential single and multistorey developments
• Education facilities
• Suburban commercial building and refurbishment
• Health
• Defence
• Industrial

Objective of Acquisition

We are planning to expand our business activities. We are aiming to increase our turnover and use website as an increased passive selling tool.

Possible company type

This is an ideal opportunity for person who can capture readers attention.

Target Market(s)

see www.bqrl.com.au

Industry/Entity Type

Construction

Requirements
Must have
• Capture peoples attention on readers zones

```html
<!DOCTYPE html>
<html lang="en">
<head>
<meta charset="utf-8">
<title>Halvern Oakridge Construction Services</title>
<link rel="stylesheet" href="https://fonts.googleapis.com/css2?family=Oswald:wght@500&family=Roboto+Condensed:wght@400;700&family=PT+Serif:wght@400;700&display=swap">
<style>
  :root {
    --night: #07080c;
    --band: #ebebeb;
    --card-head: #2f2f31;
    --card-body: #ffffff;
    --ink: #2b2b2b;
    --muted: #6f6f6f;
    --button: #2a2a2a;
    --footer: #3b3b3b;
    --footer-line: #4d4d4d;
    --gold: #e0a21c;
    --orange: #f49a1c;
    --white: #ffffff;
  }
  * { box-sizing: border-box; margin: 0; padding: 0; }
  html, body { width: 1200px; height: 900px; overflow: hidden; }
  body { position: relative; background: var(--band); font-family: "PT Serif", serif; color: var(--ink); }
  .abs { position: absolute; }

  /* Header */
  .hero {
    left: 0; top: 0; width: 1200px; height: 302px;
    background:
      radial-gradient(ellipse 380px 160px at 330px 110px, rgba(40,90,170,.45), transparent 70%),
      radial-gradient(ellipse 300px 180px at 900px 110px, rgba(150,60,30,.35), transparent 70%),
      radial-gradient(ellipse 260px 120px at 600px 40px, rgba(30,60,120,.35), transparent 70%),
      var(--night);
    border-top: 4px solid #2a2a2a;
  }
  .utility-tab {
    left: 710px; top: 0; width: 120px; height: 28px;
    background: #2c2c2e; border-radius: 0 0 10px 10px;
  }
  .brand { left: 0; top: 34px; width: 1200px; text-align: center; }
  .brand-name {
    display: inline-flex; align-items: center; gap: 8px;
    font-family: "Oswald", sans-serif; font-weight: 500; font-size: 24px;
    color: var(--white); letter-spacing: .5px; text-transform: uppercase;
  }
  .brand-mark { width: 22px; height: 22px; background: var(--white); }
  .brand-tagline {
    font-family: "Roboto Condensed", sans-serif; font-size: 11px; letter-spacing: 3px;
    color: var(--gold); text-transform: uppercase; margin-top: 2px;
  }
  .main-nav {
    left: 0; top: 91px; width: 1200px; text-align: center;
    font-family: "Roboto Condensed", sans-serif; font-weight: 700; font-size: 12.5px; color: var(--white);
  }
  .main-nav span.sep { margin: 0 8px; }
  .globe {
    left: 496px; top: 126px; width: 212px; height: 212px; border-radius: 50%;
    background: radial-gradient(circle at 40% 35%, #d8d8d8, #6b6b6b 55%, #1a1a1a 85%);
  }
  .hero-crop { left: 0; top: 302px; width: 1200px; height: 40px; background: var(--band); }
  .slogan { font-family: "Roboto Condensed", sans-serif; font-weight: 700; font-size: 20px; line-height: 24px; text-transform: uppercase; }
  .slogan .lead { color: var(--white); }
  .slogan .sub { color: #7d7d7d; }
  .slogan-left { left: 361px; top: 214px; }
  .slogan-left .sub { padding-left: 8px; }
  .slogan-right { left: 732px; top: 214px; }
  .slider-controls {
    left: 568px; top: 272px; width: 72px; height: 30px;
    background: rgba(50,50,52,.9); border-radius: 36px 36px 0 0;
  }

  /* Service cards */
  .service-card { top: 312px; width: 147px; height: 166px; background: var(--card-body); }
  .service-head { height: 64px; background: linear-gradient(#3a3a3c 0 85%, #4a4a4c 85%); position: relative; }
  .service-title {
    position: absolute; left: 4px; top: 7px;
    font-family: "Roboto Condensed", sans-serif; font-size: 13px; line-height: 15px;
    color: var(--white); text-transform: uppercase;
  }
  .service-icon { position: absolute; right: 8px; top: 8px; width: 54px; height: 50px; border-radius: 6px; }
  .service-text { padding: 17px 10px 0; font-size: 8px; line-height: 10px; text-align: center; height: 70px; }
  .read-more {
    display: block; width: 56px; height: 17px; margin: 0 auto;
    background: var(--button); color: var(--white);
    font-family: "Roboto Condensed", sans-serif; font-size: 8px; line-height: 17px; text-align: center;
  }
  .rule { left: 370px; top: 488px; width: 462px; height: 1px; background: #c9c9c9; }

  /* Welcome & testimonials */
  .section-title { font-family: "Roboto Condensed", sans-serif; font-size: 13px; text-transform: uppercase; color: var(--ink); }
  .welcome { left: 370px; top: 507px; width: 305px; font-size: 8px; line-height: 10px; }
  .welcome p { margin-top: 4px; text-align: justify; }
  .welcome .philosophy { text-align: center; margin-top: 8px; }
  .welcome .indent { padding-left: 11px; }
  .welcome .button-read { left: 617px; top: 649px; width: 57px; height: 17px; }
  .col-divider { left: 684px; top: 508px; width: 1px; height: 160px; background: #cfcfcf; }
  .testimonials { left: 693px; top: 507px; width: 137px; font-size: 7px; line-height: 8.5px; }
  .testimonials p { margin-top: 5px; }
  .testimonials hr { border: 0; border-top: 1px solid #cfcfcf; margin: 6px 0 5px; }
  .brochure {
    left: 690px; top: 635px; width: 138px; height: 28px; border-radius: 4px;
    background: linear-gradient(#ffb642, var(--orange));
    display: flex; align-items: center; gap: 6px; padding-left: 8px;
  }
  .brochure-label {
    font-family: "Roboto Condensed", sans-serif; font-weight: 700; font-size: 9.5px; line-height: 10px;
    color: #3a2200; text-transform: uppercase;
  }

  /* Footer */
  .site-footer { left: 0; top: 676px; width: 1200px; height: 224px; background: var(--footer); }
  .site-footer .section-title { color: var(--white); }
  .gallery-title { left: 374px; top: 698px; }
  .gallery-thumb { width: 90px; height: 52px; border: 2px solid #cfcfcf; }
  .footer-divider { left: 586px; top: 700px; width: 1px; height: 165px; background: var(--footer-line); }
  .message-title { left: 601px; top: 698px; }
  .field {
    left: 628px; width: 168px; border: 1px solid #5e5e5e; background: #3f3f3f;
    font-size: 6.5px; color: #8a8a8a; padding: 3px 5px;
  }
  .send {
    left: 750px; top: 847px; width: 46px; height: 18px; background: #222;
    color: var(--white); font-family: "Roboto Condensed", sans-serif; font-size: 8.5px; line-height: 18px; text-align: center;
  }
  .footer-rule { left: 370px; top: 875px; width: 462px; height: 1px; background: var(--footer-line); }
  .copyright { left: 0; top: 884px; width: 1200px; text-align: center; font-size: 7.5px; color: #7a7a7a; }
</style>
</head>
<body>

<header class="abs hero">
  <div class="abs utility-tab">
    <svg width="120" height="28" viewBox="0 0 120 28">
      <rect x="13" y="7" width="8" height="10" fill="#ddd"/>
      <rect x="55" y="7" width="9" height="9" fill="#bcd08a"/>
      <circle cx="99" cy="12" r="4.5" fill="#ccc"/>
    </svg>
  </div>
</header>

<div class="abs brand">
  <div class="brand-name"><span class="brand-mark"></span>Halvern Oakridge</div>
  <div class="brand-tagline">Construction Services</div>
</div>

<nav class="abs main-nav">
  Home<span class="sep">:</span>About us<span class="sep">:</span>Building<span class="sep">:</span>Construction Management<span class="sep">:</span>Project Management<span class="sep">:</span>Contacts
</nav>

<div class="abs globe" role="img" aria-label="Rendered silver globe showing the continents"></div>
<div class="abs hero-crop"></div>

<div class="abs slogan slogan-left"><div class="lead">Imagination</div><div class="sub">Is our power</div></div>
<div class="abs slogan slogan-right"><div class="lead">Achieve</div><div class="sub">The best results</div></div>

<div class="abs slider-controls">
  <svg width="72" height="30" viewBox="0 0 72 30">
    <path d="M25 12 L20 17 L25 22" stroke="#ddd" stroke-width="1.5" fill="none"/>
    <line x1="36" y1="8" x2="36" y2="30" stroke="#555"/>
    <path d="M47 12 L52 17 L47 22" stroke="#ddd" stroke-width="1.5" fill="none"/>
  </svg>
</div>

<main>
  <article class="abs service-card" style="left:370px">
    <div class="service-head">
      <div class="service-title">Construction<br>Management</div>
      <div class="service-icon" role="img" aria-label="Striped road barrier with warning light" style="background:linear-gradient(135deg,#f2c12e,#333)"></div>
    </div>
    <p class="service-text">We ensure every cost control is in place and project objectives are met. The benefits to you are:</p>
    <span class="read-more">Read More</span>
  </article>

  <article class="abs service-card" style="left:528px">
    <div class="service-head">
      <div class="service-title">Project<br>Management</div>
      <div class="service-icon" role="img" aria-label="Globe with an orange gear" style="background:radial-gradient(circle at 40% 40%,#49a7e0,#2f8a3c 60%,#f39a1a)"></div>
    </div>
    <p class="service-text">From start to finish; from demolition and site excavation to lock up, council sign off and tax depreciation. Our Project</p>
    <span class="read-more">Read More</span>
  </article>

  <article class="abs service-card" style="left:685px">
    <div class="service-head">
      <div class="service-title">Building</div>
      <div class="service-icon" role="img" aria-label="Open toolbox with tools" style="background:linear-gradient(160deg,#c0392b,#2a5aa8 45%,#111)"></div>
    </div>
    <p class="service-text">Planning, cost control and experience are the skills that we bring to bear on your project. Our hands on approach ensures that</p>
    <span class="read-more">Read More</span>
  </article>

  <div class="abs rule"></div>

  <section class="abs welcome">
    <h2 class="section-title">Welcome to Halvern Oakridge</h2>
    <p>We are a Sydney based Construction Company who can help with all your construction needs. The Halvern Oakridge process helps define your budget, establishes Return on Investment and reduces potential risk.</p>
    <p class="philosophy"><strong>Our philosophy is simple:</strong><br>"Deliver the project you want on time, to budget."</p>
    <p>Who uses us?</p>
    <p class="indent">Architects – to assist with costing a project, value-engineering and project implementation.</p>
    <p class="indent" style="margin-top:9px">Owner/Builders – to assist with project management, costings, work flow and final sign offs</p>
  </section>
  <span class="abs read-more button-read" style="left:617px;top:649px;width:57px">Read More</span>

  <div class="abs col-divider"></div>

  <aside class="abs testimonials">
    <h2 class="section-title" style="margin-left:1px">Testimonials</h2>
    <p style="padding-left:4px">Halvern Oakridge is a construction company with significant skills in Project and Construction Management. We will help you undertake a successful construction.</p>
    <hr>
    <p style="padding-left:4px">"The success of our Newcastle project built our confidence in the ability of Halvern Oakridge."<br>Mark Ellison Director Bramwell Constructions</p>
  </aside>

  <div class="abs brochure">
    <svg width="22" height="24" viewBox="0 0 22 24"><path d="M7 2h8v10h5L11 22 2 12h5z" fill="#2f7fc9"/></svg>
    <span class="brochure-label">Download<br>Corporate Brochure</span>
  </div>
</main>

<footer class="abs site-footer"></footer>
<h2 class="abs section-title gallery-title" style="color:var(--white)">Project Gallery</h2>
<div class="abs gallery-thumb" style="left:375px;top:726px;background:linear-gradient(90deg,#c9a27a,#e8e2da 50%,#a45a3a)" role="img" aria-label="Project interior with timber panelling"></div>
<div class="abs gallery-thumb" style="left:474px;top:726px;background:linear-gradient(135deg,#efefef,#4a3a32 60%,#ddd)" role="img" aria-label="Dark timber staircase"></div>
<div class="abs gallery-thumb" style="left:375px;top:788px;background:linear-gradient(90deg,#f2f2f2,#3c3a38 50%,#e6d6d0)" role="img" aria-label="Stairwell with white walls"></div>
<div class="abs gallery-thumb" style="left:474px;top:788px;background:linear-gradient(160deg,#e9e9e9,#6d5c50 55%,#c23a3a)" role="img" aria-label="Glass balustrade staircase with red carpet"></div>

<div class="abs footer-divider"></div>
<h2 class="abs section-title message-title" style="color:var(--white)">Quick Message</h2>
<div class="abs field" style="top:726px;height:16px">Your Name:</div>
<div class="abs field" style="top:746px;height:16px">Your E-Mail:</div>
<div class="abs field" style="top:766px;height:71px">Message:</div>
<div class="abs send">Send</div>

<div class="abs footer-rule"></div>
<p class="abs copyright">Copyright © 2012 Halvern Oakridge, All Rights Reserved</p>

</body>
</html>
```